Landscape install that wants to be known for specializing in backyard oasis

I install high end backyard retreats, I also instal water features, kitchens, patio and plants, I am not a landscaper that cuts grass for a source of income but I want to be know as someone who could be the first company you think of when you want any form of hard scape installed. Up to this point my projects have required a creative custom install that is different to cookie cutter install companies, I chose the name to reflect a company that is professional but also let customer know that I work and specialize in stone install

Target Market(s)

To everyone but more important is target customers and professionals that my company is the one they should choose

Industry/Entity Type

Landscape

Contact Information for Business Card

Dennis Markham
2847 Tindle Ct
Brenton, WI 53819
Email: www.bluefernyardcraft@quillpost.com

Requirements
Must have
• If you could help with a signature logo or something current and relevant
Nice to have
• Creative layout of the card with an great backdrop that reflects the company as cutting edge and current

```html
<!DOCTYPE html>
<html lang="en">
<head>
<meta charset="utf-8">
<title>Bluefern Yardcraft – Business Card</title>
<link href="https://fonts.googleapis.com/css2?family=Oswald:wght@500&family=Questrial&display=swap" rel="stylesheet">
<style>
  :root {
    --canvas: #ffffff;
    --card: #f1f1ec;
    --brown: #4a2412;
    --gold: #a77a1c;
    --gold-light: #d4b26a;
    --grey: #7a7a74;
    --flap-light: #f4f1e4;
    --flap-dark: #b9b294;
    --stone-dark: #5a4a42;
    --stone-mid: #8a7468;
    --water: #c9d6e2;
  }
  html, body {
    margin: 0;
    width: 990px;
    height: 1200px;
    overflow: hidden;
    background: var(--canvas);
  }
  .card {
    position: absolute;
    left: 22px;
    width: 941px;
    height: 538px;
    border-radius: 32px;
    background: var(--card);
    box-shadow: 0 3px 10px rgba(0,0,0,0.35);
    overflow: hidden;
  }
  .card--front { top: 25px; }
  .card--back  { top: 634px; }

  .brand {
    position: absolute;
    display: flex;
    align-items: center;
  }
  .brand__mark {
    background: var(--gold);
    flex: none;
  }
  .brand__name {
    font-family: "Oswald", sans-serif;
    font-weight: 500;
    color: var(--brown);
    line-height: 1.02;
    margin: 0;
  }
  .card--front .brand { left: 240px; top: 150px; gap: 30px; }
  .card--front .brand__mark { width: 72px; height: 72px; }
  .card--front .brand__name { font-size: 100px; }

  .card--back .brand { left: 40px; top: 38px; gap: 22px; }
  .card--back .brand__mark { width: 52px; height: 52px; }
  .card--back .brand__name { font-size: 74px; }

  .contact {
    position: absolute;
    left: 68px;
    top: 324px;
    font-family: "Questrial", sans-serif;
  }
  .contact__name {
    margin: 0;
    font-size: 34px;
    font-variant: small-caps;
    letter-spacing: 4px;
    color: var(--gold);
  }
  .contact__rule {
    width: 390px;
    height: 3px;
    margin: 10px 0 36px;
    background: linear-gradient(to right, var(--gold), var(--gold-light) 60%, rgba(212,178,106,0));
  }
  .contact__line {
    margin: 0 0 10px;
    font-size: 22px;
    font-variant: small-caps;
    letter-spacing: 3px;
    color: var(--grey);
  }
  .curl {
    position: absolute;
    inset: 0;
  }
</style>
</head>
<body>
  <section class="card card--front">
    <div class="brand">
      <span class="brand__mark"></span>
      <h1 class="brand__name">Bluefern<br>Yardcraft</h1>
    </div>
  </section>

  <section class="card card--back">
    <div class="brand">
      <span class="brand__mark"></span>
      <h2 class="brand__name">Bluefern<br>Yardcraft</h2>
    </div>

    <div class="contact">
      <p class="contact__name">Dennis Markham</p>
      <div class="contact__rule"></div>
      <p class="contact__line">2847 Tindle Ct</p>
      <p class="contact__line">Brenton, WI 53819</p>
      <p class="contact__line">tel: 630.555.014</p>
    </div>

    <svg class="curl" viewBox="0 0 941 538" width="941" height="538">
      <defs>
        <linearGradient id="stone-photo" x1="0" y1="0" x2="1" y2="1">
          <stop offset="0" stop-color="var(--stone-mid)"/>
          <stop offset="0.45" stop-color="var(--water)"/>
          <stop offset="0.7" stop-color="var(--stone-mid)"/>
          <stop offset="1" stop-color="var(--stone-dark)"/>
        </linearGradient>
        <linearGradient id="flap-shade" x1="0" y1="0" x2="1" y2="0.3">
          <stop offset="0" stop-color="var(--flap-light)"/>
          <stop offset="0.55" stop-color="#e2ddc8"/>
          <stop offset="1" stop-color="var(--flap-dark)"/>
        </linearGradient>
      </defs>
      <path role="img" aria-label="Photo of a stone waterfall cascading over layered rocks"
            d="M941 30 L941 538 L478 538 C680 380 860 200 941 30 Z"
            fill="url(#stone-photo)"/>
      <path class="curl__flap"
            d="M905 0 C760 90 600 300 462 538 L478 538 C680 380 860 200 941 30 L941 0 Z"
            fill="url(#flap-shade)"/>
      <path d="M905 0 C760 90 600 300 462 538"
            fill="none" stroke="rgba(0,0,0,0.12)" stroke-width="2"/>
    </svg>
  </section>
</body>
</html>
```